Safety training business card design

We need a buisness card design and logo for a small buisness that provides safety training through out the mining and civil construction industries. We provide first aid , confined space working at heights , machinery tickets, chainsaw, four wheel drive and four wheel motorbike training. We would like to use the design colors of navy blue, Fluro or lime green and white .

Industry/Entity Type

Construction

Contact Information for Business Card

Rillford Groundworks & Training , Neville Ormsby, rillford.skills@mailbox-example.net, ph 0481065374 abn 47 806 315 914

```html
<!DOCTYPE html>
<html lang="en">
<head>
<meta charset="utf-8">
<title>Rillford Groundworks &amp; Training – Business Card</title>
<link rel="stylesheet" href="https://fonts.googleapis.com/css2?family=Michroma&family=Questrial&display=swap">
<style>
  :root {
    --navy: #15294a;
    --orange: #f28c1c;
    --white: #ffffff;
    --backdrop: #e8e5e0;
    --card-w: 540px;
    --card-h: 309px;
  }
  * { box-sizing: border-box; margin: 0; padding: 0; }
  html, body {
    width: 1200px;
    height: 784px;
    overflow: hidden;
    background: var(--backdrop);
  }
  .canvas {
    width: 1200px;
    height: 784px;
    display: flex;
    align-items: center;
    justify-content: center;
    gap: 40px;
  }
  .card {
    width: var(--card-w);
    height: var(--card-h);
    position: relative;
    overflow: hidden;
    box-shadow: 0 6px 18px rgba(0,0,0,0.18);
  }

  /* Front */
  .card-front { background: var(--navy); }
  .front-header {
    position: absolute;
    inset: 0 0 auto 0;
    height: 172px;
    background: var(--white);
  }
  .header-rule {
    position: absolute;
    left: 300px;
    right: 0;
    top: 108px;
    height: 4px;
    background: var(--orange);
  }
  .brand {
    position: absolute;
    left: 28px;
    top: 128px;
    display: flex;
    align-items: center;
    gap: 10px;
  }
  .brand-square {
    width: 16px;
    height: 16px;
    background: var(--orange);
  }
  .brand-name {
    font-family: "Michroma", sans-serif;
    font-size: 15px;
    letter-spacing: 1.5px;
    text-transform: uppercase;
    color: var(--navy);
    white-space: nowrap;
  }
  .header-stripe {
    position: absolute;
    left: 0;
    right: 0;
    top: 172px;
    height: 7px;
    background: var(--orange);
  }
  .contact {
    position: absolute;
    left: 34px;
    top: 192px;
    font-family: "Questrial", sans-serif;
    color: var(--white);
  }
  .contact-name {
    font-size: 20px;
    color: var(--orange);
    margin-bottom: 10px;
  }
  .contact-line {
    display: flex;
    align-items: center;
    gap: 8px;
    font-size: 18px;
    line-height: 1.3;
  }
  .contact-line.email { font-size: 15px; }
  .contact-line svg { width: 18px; height: 18px; flex: none; }
  .abn {
    font-size: 13px;
    margin-left: 26px;
    margin-top: 2px;
  }

  /* Back */
  .card-back {
    background: var(--navy);
    display: flex;
    align-items: center;
    justify-content: center;
  }
  .services {
    list-style: none;
    text-align: center;
    font-family: "Michroma", sans-serif;
    font-size: 12.5px;
    letter-spacing: 1.6px;
    line-height: 1.75;
    text-transform: uppercase;
    color: var(--orange);
  }
</style>
</head>
<body>
  <main class="canvas">
    <section class="card card-back" aria-label="Card back">
      <ul class="services">
        <li>First Aid</li>
        <li>Confined Space Working at Heights</li>
        <li>Machinery Tickets</li>
        <li>Chainsaw</li>
        <li>Four Wheel Drive</li>
        <li>and</li>
        <li>Four Wheel Motorbike</li>
        <li>Training</li>
      </ul>
    </section>

    <section class="card card-front" aria-label="Card front">
      <div class="front-header">
        <div class="header-rule"></div>
        <div class="brand">
          <span class="brand-square"></span>
          <span class="brand-name">Rillford Groundworks &amp; Training</span>
        </div>
      </div>
      <div class="header-stripe"></div>
      <div class="contact">
        <p class="contact-name">Neville Ormsby</p>
        <p class="contact-line phone">
          <svg viewBox="0 0 24 24" aria-hidden="true"><path fill="#f28c1c" d="M6.6 10.8a15 15 0 0 0 6.6 6.6l2.2-2.2a1 1 0 0 1 1-.25 11.4 11.4 0 0 0 3.6.57 1 1 0 0 1 1 1V20a1 1 0 0 1-1 1A17 17 0 0 1 3 4a1 1 0 0 1 1-1h3.5a1 1 0 0 1 1 1c0 1.25.2 2.45.57 3.57a1 1 0 0 1-.25 1z"/></svg>
          <span>0481065374</span>
        </p>
        <p class="contact-line email">
          <svg viewBox="0 0 24 24" aria-hidden="true"><rect x="2" y="5" width="20" height="14" rx="2" fill="#f28c1c"/><path d="M3 6l9 7 9-7" fill="none" stroke="#15294a" stroke-width="1.8"/></svg>
          <span>rillford.skills@mailbox-example.net</span>
        </p>
        <p class="abn">abn 47 806 315 914</p>
      </div>
    </section>
  </main>
</body>
</html>
```